Rebrand of 3 bottle labels for nail polish brand

The task is to make a rebranding of our current gel nail polish bottle design. We have become one of the leading european nail polish brand, so we want to improve the quality of the label design to a more scandinavian and minimalistic bottle design, which stille has to be recognisable and unique.

We have attached a more detailed description of the rebranding instructions for our gel polish bottles called "bottle task".
Updates

The Labels should not be just Black and White as stated. But should be mainly Black and White and then some of our color as explained in the uploaded file.

Target Market(s)

Girls and women age 18-55 Northern Europe

Industry/Entity Type

Cosmetic/ Nail Gel Polish

Colors

Designer to choose only greyscale colors for use in the design.

Requirements
Must have
• See attched design instruction
Nice to have
• Moderne, Minimalist, Recognizable and Unique look
Should not have
• Too many elements, too busy design

```html
<!DOCTYPE html>
<html lang="en">
<head>
<meta charset="utf-8">
<title>velmora — Base Coat Label</title>
<link rel="stylesheet" href="https://fonts.googleapis.com/css2?family=Montserrat:wght@300;400;600;700&display=swap">
<style>
  :root {
    --canvas: #ffffff;
    --label-black: #000000;
    --ink-white: #ffffff;
    --rose-taupe: #bf9a8f;
  }
  * { margin: 0; padding: 0; box-sizing: border-box; }
  html, body {
    width: 1200px;
    height: 1003px;
    overflow: hidden;
    background: var(--canvas);
  }
  .label {
    position: absolute;
    left: 100px;
    top: 73px;
    width: 1000px;
    height: 857px;
    background: var(--label-black);
    color: var(--ink-white);
    font-family: "Montserrat", sans-serif;
  }
  .pattern-strip {
    position: absolute;
    right: 0;
    top: 0;
    width: 180px;
    height: 100%;
    background: var(--rose-taupe);
  }
  .wordmark {
    position: absolute;
    left: 252px;
    top: 118px;
    font-weight: 300;
    font-size: 124px;
    line-height: 1;
    letter-spacing: 2px;
    color: var(--ink-white);
  }
  .product-name {
    position: absolute;
    left: 264px;
    top: 354px;
    font-weight: 700;
    font-size: 44px;
    letter-spacing: 4px;
    line-height: 1;
  }
  .product-type {
    position: absolute;
    left: 264px;
    top: 414px;
    font-weight: 400;
    font-size: 44px;
    letter-spacing: 6px;
    line-height: 1;
  }
  .shade-number {
    position: absolute;
    left: 256px;
    top: 530px;
    font-weight: 600;
    font-size: 170px;
    line-height: 1;
    letter-spacing: -4px;
    color: var(--rose-taupe);
  }
  .shade-tag {
    position: absolute;
    left: 264px;
    top: 704px;
    width: 202px;
    height: 62px;
    background: var(--rose-taupe);
    color: var(--ink-white);
    font-size: 34px;
    font-weight: 400;
    letter-spacing: 6px;
    display: flex;
    align-items: center;
    justify-content: center;
    padding-left: 6px;
  }
  .divider {
    position: absolute;
    left: 527px;
    top: 539px;
    width: 4px;
    height: 236px;
  }
  .volume {
    position: absolute;
    left: 593px;
    top: 542px;
    font-weight: 400;
    font-size: 40px;
    line-height: 56px;
  }
</style>
</head>
<body>
  <section class="label">
    <div class="wordmark">velmora</div>

    <div class="product-name">BASE COAT</div>
    <div class="product-type">SOAK OFF UV/LED</div>

    <div class="shade-number">01</div>
    <div class="shade-tag">RUBBER</div>

    <svg class="divider" viewBox="0 0 4 236" aria-hidden="true">
      <line x1="2" y1="0" x2="2" y2="236" stroke="#ffffff" stroke-width="3" stroke-dasharray="8 8"/>
    </svg>

    <div class="volume">15ml ℮<br>0.5oz</div>

    <div class="pattern-strip" role="img" aria-label="Vertical band of repeating rose-taupe petal and diamond pattern"></div>
  </section>
</body>
</html>
```